Business Card Design Project

We require a business card template to cover basic contact information - our company logo, names of employees, title, mobile and email.

Target Market(s)

Corporate

Industry/Entity Type

Business

Font styles to use
Sans Serif

Requirements
Nice to have
• Thinking it would be great just to have the logo taking up approximately half the space (so it goes as far across the top of the card as possible) and then contact details in the lower half of the card. Keen just to use only the two colours in the logo, on a white background.
Should not have
• No fussy drawings

```html
<!DOCTYPE html>
<html lang="en">
<head>
<meta charset="utf-8">
<title>Hivemoor business card</title>
<link rel="stylesheet" href="https://fonts.googleapis.com/css2?family=Open+Sans:ital,wght@0,400;0,600;1,400&display=swap">
<style>
  :root {
    --card-grey: #cbcbcb;
    --band-deep: #003135;
    --brand-teal: #2fa5b5;
    --name-blue: #0f6aa0;
    --text-deep: #0a3a3e;
  }
  html, body {
    margin: 0;
    padding: 0;
    overflow: hidden;
  }
  .card {
    position: relative;
    width: 1200px;
    height: 686px;
    background: var(--card-grey);
    font-family: "Open Sans", sans-serif;
    overflow: hidden;
  }
  .brand-band {
    position: absolute;
    left: 16px;
    top: 0;
    width: 1168px;
    height: 340px;
    background: var(--band-deep);
    box-shadow: 0 4px 6px rgba(0, 0, 0, 0.45);
  }
  .brand-name {
    position: absolute;
    left: 78px;
    top: 60px;
    margin: 0;
    font-size: 150px;
    font-weight: 600;
    letter-spacing: -2px;
    line-height: 1;
    color: var(--brand-teal);
  }
  .person {
    position: absolute;
    left: 0;
    top: 384px;
    width: 1200px;
    text-align: center;
  }
  .person-name {
    margin: 0;
    font-size: 34px;
    font-weight: 600;
    letter-spacing: -0.5px;
    color: var(--name-blue);
  }
  .person-title {
    margin: 2px 0 0;
    font-size: 27px;
    font-style: italic;
    letter-spacing: -0.5px;
    color: var(--text-deep);
  }
  .contact {
    position: absolute;
    right: 40px;
    top: 572px;
    text-align: center;
    font-size: 28px;
    font-style: italic;
    letter-spacing: -0.5px;
    line-height: 36px;
    color: var(--text-deep);
  }
  .contact p {
    margin: 0;
  }
</style>
</head>
<body>
  <div class="card">
    <header class="brand-band">
      <h1 class="brand-name">Hivemoor</h1>
    </header>
    <section class="person">
      <p class="person-name">Marisol T Dacanay</p>
      <p class="person-title">Creative Research &amp; Development</p>
    </section>
    <section class="contact">
      <p class="contact-email">marisoldacanay@mailnook.com</p>
      <p class="contact-phone">148.5521.0736</p>
    </section>
  </div>
</body>
</html>
```